Adlinks Landing Page - DESIGN ONLY! PSD File

BACKGROUND:
Our website www.trailkit.com.au (running on Storlane) has a range of outdoor equipment being sold online. One of the products we specialize in is generators.
We are after a content landing page designed for Bluefin Adlinks to link to. This page should be focused on converting customers to sales as most customers at this stage of buying are ready to buy. We would like this page to focus on a combination of a professional graphic design and some text. The way it is laid out is open to your own experience, we just want it to look professional and have the right info for customers to convert.
THE BRIEF:
The page will include the range of products in the generator category that can be found here:
http://www.trailkit.com.au/generators.html
This page should include all the products within this category and should fit into to the color scheme and look of the website.
Most focus on the product should be placed in this order of priority, with special focus on the first two:
1. 2kva RRP: $1099 down to $499
2. 3.5kva RRP: $1399 down to $780
3. 3.5kva electric start RRP: $1599 down to $890
4. 4.4kva RRP: $1899 down to $950 (not currently listed, images will be provided soon)
5. 5kva RRP: $1999 down to $1150
The page can include a variety of graphic design, text and hyperlinks (or image clickable links), so please take this into account when making the graphics design.
The page must be discount oriented and include prices of each product as well as its original RRP price (crossed out), possible 'sale' graphics, and 'buy now' buttons linking to the product.
An example area this should fit within is the the column the products are on this page:
Other notes:
Our prices are truly bargains and the lowest in the market, so don't be afraid to express that in the design; texts like "Massive Sale" , "Priced to Clear Out" , "Won't Last Long at this Price"
Product images can be grabbed off the products here:
Deliverable will be a PSD file of the finished design.
We need these contact numbers included somewhere on this page:
NSW/ACT: 02 8555 0142
VIC/TAS: 03 9555 0176
SA: 08 7555 0193
NT/WA: 08 85550127

```html
<!DOCTYPE html>
<html lang="en">
<head>
<meta charset="utf-8">
<title>Generators Clearance Sale</title>
<link href="https://fonts.googleapis.com/css2?family=Arimo:wght@400;700&family=Maven+Pro:wght@400;500;600&display=swap" rel="stylesheet">
<style>
:root{
  --earth:#c98a4e;
  --white:#ffffff;
  --line:#8a8a8a;
  --text:#111111;
  --muted:#9a9a9a;
  --link:#0a0a6a;
  --side-text:#555555;
  --sky:#7bb8e0;
  --sky-deep:#4f92c4;
  --stripe:#d2d2d2;
  --sale:#d9182c;
  --save:#d0101c;
  --btn-top:#f8f8f8;
  --btn-bottom:#d8d8d8;
  --btn-border:#9a9a9a;
  --photo-red:#d8262a;
  --photo-dark:#2b2b2b;
}
*{margin:0;padding:0;box-sizing:border-box}
html,body{width:1095px;height:1200px;overflow:hidden}
body{background:var(--earth);font-family:"Arimo",Arial,sans-serif;position:relative}
.abs{position:absolute}
.page{position:absolute;left:153px;top:0;width:833px;height:1200px;background:var(--white)}
.crumb{left:9px;top:8px;font-size:9.5px;color:var(--text)}
.crumb a{color:#5a8a1a}
.box{border:1px solid #dcdcdc;background:var(--white);left:9px;width:210px}
.box h2{position:absolute;left:10px;font-size:14.5px;font-weight:700;color:var(--text);display:flex;align-items:center;gap:5px}
.box h2 i{display:inline-block;width:12px;height:9px;border:1px solid #6a7fa6;border-radius:2px;background:#e7eef8}
.cat-list{position:absolute;left:10px;width:191px;list-style:none}
.cat-list li{height:24.8px;border-bottom:1px solid var(--line);font-size:12.5px;color:var(--side-text);padding:4px 0 0 19px;position:relative}
.cat-list li::before{content:"";position:absolute;left:5px;top:11px;width:3px;height:3px;border-radius:50%;background:var(--side-text)}
.special{position:absolute;width:96px}
.special .ph{width:86px;height:64px;border-radius:2px}
.special a{display:block;margin-top:17px;font-size:10.5px;font-weight:700;color:var(--link);text-decoration:underline;line-height:13.7px}
.special .price{margin-top:8px;font-size:11px;font-weight:700;color:var(--text)}
.main{position:absolute;left:227px;top:27px;width:597px;height:1166px;border:1px solid #c9c9c9;background:var(--white);font-family:"Maven Pro",sans-serif}
.hero{position:absolute;left:0;top:0;width:595px;height:176px;overflow:hidden;background:linear-gradient(90deg,var(--sky-deep),var(--sky))}
.hero h1{position:absolute;left:24px;top:17px;font-size:33px;font-weight:500;color:var(--white);white-space:nowrap}
.hero .tag{position:absolute;left:24px;top:54px;font-size:20px;font-weight:500;color:var(--white);line-height:25px}
.hero .ship{position:absolute;left:24px;top:144px;font-size:12px;font-weight:600;color:#1a2a3a}
.product{position:absolute;text-align:center}
.product h3{font-weight:500;color:var(--text);line-height:31px;font-size:26px;white-space:nowrap}
.product .sub{font-size:13px;font-weight:600;color:var(--text);line-height:14px}
.product .desc{margin-top:19px;font-size:13px;color:var(--muted);line-height:16px}
.prices{margin-top:13px;font-size:13.5px;font-weight:500;line-height:16px}
.prices .now{color:var(--text)}
.prices .was{color:var(--muted);text-decoration:line-through}
.prices .save{color:var(--save)}
.btn{display:inline-block;margin-top:6px;width:95px;height:27px;border:1px solid var(--btn-border);border-radius:3px;background:linear-gradient(var(--btn-top),var(--btn-bottom));font-family:"Maven Pro",sans-serif;font-size:12.5px;font-weight:600;color:#333;line-height:25px}
.rule{position:absolute;left:32px;width:547px;height:1px;background:#b5b5b5}
.shot{position:absolute;border-radius:14px}
.shot.red{background:radial-gradient(circle at 40% 40%,#f04040,var(--photo-red) 60%,#9c1518)}
.shot.dark{background:linear-gradient(90deg,var(--photo-dark) 0 55%,var(--photo-red) 55%)}
.trio h3{font-size:13.5px;font-weight:600;line-height:16.5px}
.trio .prices{margin-top:6px}
.trio .btn{margin-top:6px}
.band{position:absolute;left:0;bottom:0;width:595px;height:88px;overflow:hidden;background:linear-gradient(90deg,var(--sky),#c3dbee 40%,#d4d4d4 40%)}
.phones{position:absolute;left:462px;top:28px;font-size:10px;color:var(--white);line-height:12.4px;letter-spacing:.2px}
</style>
</head>
<body>
<div class="page">
  <div class="abs crumb"><a>Home</a> / <b>Generators</b></div>

  <div class="abs box" style="top:27px;height:385px">
    <h2 style="top:11px"><i></i>CATEGORIES</h2>
    <ul class="cat-list" style="top:30px">
      <li>Camper Trailers</li><li>Camping &amp; Outdoors</li><li>Awnings</li><li>Tents</li>
      <li>Carvanning &amp; 4WD</li><li>Jacks</li><li>Winches</li><li>Generators</li>
      <li>Inverters &amp; Regulators</li><li>Lighting</li><li>Refrigeration</li>
      <li>Fixed Solar Panels</li><li>Portable Solar Panels</li><li>Solar</li>
    </ul>
  </div>

  <div class="abs box" style="top:425px;height:491px;overflow:hidden">
    <h2 style="top:10px"><i></i>SPECIALS</h2>
    <div class="special" style="left:14px;top:51px">
      <div class="ph" style="background:linear-gradient(#f2f2f2,#cfcfcf)" role="img" aria-label="Portable fridge freezer photo"></div>
      <a>Quellbrook 45L Portable Fridge Freezer</a>
      <div class="price">$519.00</div>
    </div>
    <div class="special" style="left:110px;top:51px">
      <div class="ph" style="background:linear-gradient(#a9adb2,#5a5e63)" role="img" aria-label="Hard roof top tent photo"></div>
      <a>Automatic Hard Roof Top Tent</a>
      <div class="price">$2,899.00</div>
    </div>
    <ul class="cat-list" style="top:211px">
      <li>Tents</li><li>Carvanning &amp; 4WD</li><li>Jacks</li><li>Winches</li><li>Generators</li>
      <li>Inverters &amp; Regulators</li><li>Lighting</li><li>Refrigeration</li>
      <li>Fixed Solar Panels</li><li>Portable Solar Panels</li><li>Solar</li>
    </ul>
  </div>

  <div class="abs box" style="top:929px;height:280px">
    <h2 style="top:10px"><i></i>SPECIALS</h2>
    <div class="special" style="left:14px;top:44px">
      <div class="ph" style="background:linear-gradient(#ffffff,#d7d7d7)" role="img" aria-label="4WD vehicle with side awning photo"></div>
      <a>4WD Side Awning (2m x 1.7m)</a>
      <div class="price">$165.00</div>
    </div>
    <div class="special" style="left:110px;top:44px">
      <div class="ph" style="background:radial-gradient(#fbff7a,#d8df10)" role="img" aria-label="Yellow LED strip lights photo"></div>
      <a>12VDC 5m Yellow LED Adhesive Strip Lights</a>
      <div class="price">$59.00</div>
    </div>
  </div>

  <div class="main">
    <div class="hero">
      <svg class="abs" style="left:0;top:0" width="595" height="176" viewBox="0 0 595 176">
        <polygon points="470,60 560,0 595,0 595,10 500,60 560,176 540,176" fill="var(--stripe)"/>
        <polygon points="500,60 595,10 595,176 560,176" fill="var(--sky)" opacity=".5"/>
        <circle cx="456" cy="98" r="47" fill="var(--sale)"/>
        <text x="456" y="106" text-anchor="middle" transform="rotate(-18 456 98)" fill="#fff" font-family="Maven Pro, sans-serif" font-size="23" font-weight="600">SALE.</text>
      </svg>
      <h1>Massive Clearance Sale</h1>
      <div class="tag">Priced to clear out quick!<br>Won’t last long at this price!</div>
      <div class="ship">Delivery $15 Australia Wide</div>
    </div>

    <div class="shot red" style="left:86px;top:259px;width:171px;height:184px" role="img" aria-label="Red 2kVA inverter generator photo"></div>
    <div class="product" style="left:303px;top:193px;width:300px">
      <h3>Silent 2kVA Pure Sine<br>Wave Inverter<br>Generator</h3>
      <div class="sub">with a DC alternator</div>
      <div class="desc">Powerful enough to be used professionally<br>whilst maintaining portabilty.</div>
      <div class="prices"><div class="now">Now Only $499</div><div class="was">Was $1099</div><div class="save">Save $600</div></div>
      <div class="btn">Add to Cart</div>
    </div>
    <div class="rule" style="top:467px"></div>

    <div class="product" style="left:12px;top:506px;width:320px">
      <h3>Silent 3.5kVA Pure Sine<br>Wave Inverter Generator</h3>
      <div class="sub">with a DC alternator</div>
      <div class="desc">Powerful enough to be used professionally<br>whilst maintaining portabilty.</div>
      <div class="prices"><div class="now">Now Only $780</div><div class="was">Was $1399</div><div class="save">Save $619</div></div>
      <div class="btn">Add to Cart</div>
    </div>
    <div class="shot red" style="left:372px;top:524px;width:176px;height:189px" role="img" aria-label="Red 3.5kVA inverter generator photo"></div>
    <div class="rule" style="top:758px"></div>

    <div class="shot red" style="left:35px;top:772px;width:140px;height:126px" role="img" aria-label="Red 3.5kVA electric start generator photo"></div>
    <div class="shot dark" style="left:238px;top:772px;width:136px;height:133px" role="img" aria-label="Black and red 4.4kVA generator photo"></div>
    <div class="shot dark" style="left:431px;top:772px;width:136px;height:133px" role="img" aria-label="Black and red 5kVA generator photo"></div>

    <div class="product trio" style="left:15px;top:922px;width:180px">
      <h3>Silent 3.5kVA Pure Sine<br>Wave Inverter Generator<br>Electric Start + Remote</h3>
      <div class="prices"><div class="now">Now Only $890</div><div class="was">Was $1599</div><div class="save">Save $709</div></div>
      <div class="btn">Add to Cart</div>
    </div>
    <div class="product trio" style="left:219px;top:922px;width:180px">
      <h3>Silent 4.4kVA Pure Sine<br>Wave Inverter Generator<br>Electric Start + Remote</h3>
      <div class="prices"><div class="now">Now Only $950</div><div class="was">Was $1899</div><div class="save">Save $949</div></div>
      <div class="btn">Add to Cart</div>
    </div>
    <div class="product trio" style="left:412px;top:922px;width:180px">
      <h3>Silent 5kVA Pure Sine<br>Wave Inverter Generator<br>Electric Start + Remote</h3>
      <div class="prices"><div class="now">Now Only $1150</div><div class="was">Was $1999</div><div class="save">Save $849</div></div>
      <div class="btn">Add to Cart</div>
    </div>

    <div class="band">
      <svg class="abs" style="left:0;top:0" width="595" height="88" viewBox="0 0 595 88">
        <polygon points="0,0 180,0 206,35 166,88 0,88" fill="var(--sky)"/>
        <polygon points="180,0 195,0 218,35 183,88 166,88 206,35" fill="var(--sky-deep)"/>
        <polygon points="195,0 595,0 595,88 183,88 218,35" fill="var(--stripe)"/>
      </svg>
      <div class="phones">NSW/ACT: 02 8555 0142<br>VIC/TAS: 03 9555 0176<br>SA: 08 7555 0193<br>NT/WA: 08 85550127</div>
    </div>
  </div>
</div>
</body>
</html>
```